Flyer/Brochure for a Young Non-Profit

We want to revamp our flyer to complement our new logo and to reflect a greater global appeal. Our company is a non-profit that exchanges students, interns and volunteers across the globe.

We are looking for the following elements:
1. Elegance
2. Brevity
3. Vibrancy
4. Inspirational

We are looking for the following layouts:
1. Single gate-fold, or
2. Die-cut Z Fold
(http://www.foldmerrow.net/15-brochure-fold-types/)

The final design should also look good as a single jpeg or pdf as an email attachment.

The flyer will be given to both our potential young participants and the senior management of our partners.

Please use the uploaded as materials for content (01 word doc and assortment of photos).

Target Market(s)

Students from 15 and above to adults up to 30 years of age. Senior management of commercial companies and other non-profit organizations.

Industry/Entity Type

Non-Profit

Font styles to use
Serif

Requirements
Must have
• Attached contents.

```html
<!DOCTYPE html>
<html lang="en">
<head>
<meta charset="utf-8">
<title>Kirava Art &amp; Exchange — Brochure</title>
<link rel="stylesheet" href="https://fonts.googleapis.com/css2?family=Oswald:wght@400;500;600&family=Lato:ital,wght@0,400;0,700;0,900;1,700&display=swap">
<style>
  :root{
    --page:#e9e6e1;
    --blue:#1b86cc;
    --blue-deep:#0a5a9c;
    --red:#d5121d;
    --yellow:#f5c300;
    --grey:#efefef;
    --ink:#3a3a3a;
    --white:#ffffff;
  }
  *{box-sizing:border-box;margin:0;padding:0}
  html,body{width:900px;height:1200px;overflow:hidden;background:var(--page)}
  body{position:relative;font-family:"Lato",Arial,sans-serif;color:var(--ink)}
  .spread{position:absolute;left:90px;width:720px;overflow:hidden;background:var(--grey);box-shadow:0 4px 14px rgba(0,0,0,.18)}
  .spread--outer{top:60px;height:515px}
  .spread--inner{top:635px;height:510px}
  .spread svg.art{position:absolute;inset:0;width:100%;height:100%}
  .block{position:absolute}
  .tab{display:inline-block;font-family:"Oswald",Arial,sans-serif;font-weight:500;font-size:14px;line-height:1;padding:3px 14px 3px 8px;border-radius:0 12px 12px 0;background:linear-gradient(#ffd933,var(--yellow));color:var(--blue-deep)}
  .tab--white{color:var(--white)}
  .lead{color:var(--blue-deep);font-weight:700;font-size:9px;line-height:1.25}
  .body-copy{font-size:7.6px;line-height:1.33;text-align:justify;color:var(--ink)}
  .body-copy p+p{margin-top:2px}
  .contact h3{font-family:"Lato",sans-serif;font-weight:700;font-size:9.5px;color:var(--yellow);margin-bottom:3px}
  .contact p{font-size:8.6px;line-height:1.2;color:var(--white)}
  .contact .line{display:flex;align-items:center;gap:4px;font-weight:700}
  .icon{width:9px;height:9px;flex:none}
  .dot{width:8px;height:8px;border-radius:50%;background:var(--white);flex:none}
  .brand{display:flex;align-items:center;gap:6px;font-family:"Lato",sans-serif;font-weight:900;color:#4a4a4a}
  .brand .mark{width:16px;height:16px;border-radius:50%;background:var(--red);flex:none}
  .brand span{line-height:1.05}
  .headline{font-family:"Oswald",Arial,sans-serif;text-align:center;line-height:1}
  .headline .one{font-weight:400;font-size:28px;color:var(--blue);letter-spacing:.5px}
  .headline .two{font-weight:600;font-size:27px;color:#1e1e1e;margin-top:3px}
  .web{position:absolute;left:523px;top:467px;width:160px;height:24px;border-radius:12px;background:linear-gradient(#ffdf4a,var(--yellow));color:var(--blue-deep);font-weight:900;font-size:14px;text-align:center;line-height:24px}
  .partners-label{position:absolute;left:382px;top:263px;width:118px;height:21px;background:var(--yellow);font-family:"Oswald",sans-serif;font-weight:500;font-size:12px;color:#1e1e1e;text-align:center;line-height:21px}
  .partner{position:absolute;left:384px;width:112px;text-align:center;font-size:7.8px;font-weight:700;color:var(--blue-deep);line-height:1.25}
  .badge-square{width:22px;height:22px;margin:0 auto 6px;background:#efe3b9}
  .badge-circle{width:44px;height:44px;margin:0 auto 6px;border-radius:50%;border:2px solid #555}
  .programs{list-style:none}
  .programs li{font-size:8px;font-weight:700;font-style:italic;color:var(--white);line-height:1.65;display:flex;align-items:center;gap:5px}
  .programs li::before{content:"";width:5px;height:5px;background:var(--yellow);flex:none}
  .white-copy{font-size:8.4px;font-weight:700;color:var(--white);line-height:1.3}
  .sub{font-weight:700;font-size:10px;color:var(--yellow)}
</style>
</head>
<body>

<!-- Outer spread -->
<section class="spread spread--outer">
  <svg class="art" viewBox="0 0 720 515" preserveAspectRatio="none">
    <defs>
      <linearGradient id="gGrey" x1="0" y1="0" x2="1" y2="1"><stop offset="0" stop-color="#f7f7f7"/><stop offset="1" stop-color="#d9d9d9"/></linearGradient>
      <linearGradient id="gBlue" x1="0" y1="0" x2="0" y2="1"><stop offset="0" stop-color="#2aa3df"/><stop offset="1" stop-color="#0b64ad"/></linearGradient>
      <linearGradient id="gRed" x1="0" y1="0" x2="0" y2="1"><stop offset="0" stop-color="#ec2a2f"/><stop offset="1" stop-color="#b30d16"/></linearGradient>
      <linearGradient id="pClass" x1="0" y1="0" x2="0" y2="1"><stop offset="0" stop-color="#d8b59a"/><stop offset=".5" stop-color="#6f93b4"/><stop offset="1" stop-color="#7a4c2c"/></linearGradient>
      <linearGradient id="pPark" x1="0" y1="0" x2="1" y2="1"><stop offset="0" stop-color="#5e8a45"/><stop offset="1" stop-color="#9aaa8c"/></linearGradient>
      <linearGradient id="pKids" x1="0" y1="0" x2="1" y2="1"><stop offset="0" stop-color="#a6c3cf"/><stop offset=".6" stop-color="#d7a9b5"/><stop offset="1" stop-color="#3f4f66"/></linearGradient>
    </defs>
    <rect x="0" y="0" width="242" height="515" fill="url(#gGrey)"/>
    <rect x="242" y="0" width="240" height="515" fill="url(#gBlue)"/>
    <rect x="482" y="0" width="238" height="515" fill="url(#gGrey)"/>
    <path d="M0,2 Q130,-4 242,10 L242,16 Q130,4 0,9 Z" fill="var(--yellow)"/>
    <path role="img" aria-label="Photo: group of volunteers posing in a green park" d="M242,0 H482 V62 Q380,102 242,88 Z" fill="url(#pPark)"/>
    <path d="M242,88 Q380,102 482,62" fill="none" stroke="var(--yellow)" stroke-width="6"/>
    <path role="img" aria-label="Faint photo: volunteer with an elephant" d="M300,200 H470 V390 H300 Z" fill="#ffffff" opacity=".12"/>
    <path d="M0,335 Q120,312 242,342 L242,352 Q120,322 0,345 Z" fill="var(--white)"/>
    <path role="img" aria-label="Photo: children seated in a classroom with a teacher" d="M0,345 Q120,322 242,352 V515 H0 Z" fill="url(#pClass)"/>
    <path d="M242,420 C330,465 420,455 482,402 C560,340 640,430 720,395 V515 H242 Z" fill="url(#gRed)"/>
    <path role="img" aria-label="Red-toned photo: smiling child" d="M255,448 C300,462 340,468 370,466 V515 H255 Z" fill="#9e0a12" opacity=".7"/>
    <path d="M500,205 C560,178 650,178 720,160 V180 C650,198 565,198 515,225 C500,300 495,400 505,470 L492,470 C482,390 486,290 500,205 Z" fill="url(#gRed)"/>
    <path role="img" aria-label="Photo: teacher with young children on a bench" d="M515,225 C565,198 650,198 720,180 V450 C640,470 570,470 505,465 C495,400 500,300 515,225 Z" fill="url(#pKids)"/>
    <path d="M505,465 C570,470 640,470 720,450" fill="none" stroke="#b30d16" stroke-width="8"/>
  </svg>

  <div class="block" style="left:0;top:12px;width:240px">
    <span class="tab">Our Mission:</span>
    <p class="lead" style="margin:7px 10px 0 18px">Grow people and bridges of understanding and cooperation between cultures across the world.</p>
    <span class="tab tab--white" style="margin-top:10px">Who We Are:</span>
    <div class="body-copy" style="margin:7px 10px 0 18px">
      <p>Established in 2005, Kirava Art and Culture Exchange works with established partners from across 23 countries from our offices in Singapore and Shanghai, China.</p>
      <p>From country to country, our interns and volunteers have been placed in a wide range of experiences; from hospitality to hospitals, from schools to scuba-diving, from wild life and environmental conservation to humanitarian and social, community welfare, from small businesses to large commercial companies, from hotel to locals homes.</p>
      <p>Both our host partners and participants have reaped a multitude of benefits through the matching of needs and skills, and efforts. Yet, be it helping nurse an injured bird back to health, or raising awareness for the disabled or disadvantaged; be it guiding young change-makers or young ones in language classes, be it helping build a brand new marketing campaign online or having a hand in raising a building, all of us are able to breathe a little easier, grow a bit more and smile a bit more through these new beautiful relationships.</p>
      <p>Join us here at Kirava to open minds and touch hearts across the globe.</p>
    </div>
  </div>

  <div class="block" style="left:242px;top:78px"><span class="tab" style="font-size:15px;padding:4px 16px 4px 10px">Contact Us</span></div>

  <div class="block contact" style="left:262px;top:115px;width:210px">
    <h3>Singapore Office:</h3>
    <p>12-08 B, 40 Riverside Crescent<br>Riverside 40, Singapore 700418</p>
    <p class="line"><svg class="icon" viewBox="0 0 10 10"><rect x="0.5" y="1.5" width="9" height="7" fill="var(--yellow)"/><path d="M0.5,1.5 L5,5.5 L9.5,1.5" stroke="#0a5a9c" fill="none"/></svg>apply@kirava.org</p>
    <p class="line"><svg class="icon" viewBox="0 0 10 10"><rect width="10" height="10" rx="2" fill="var(--yellow)"/><path d="M3,2 L4,4 L3.5,5 Q4.5,6.5 5.5,6.5 L6,6 L8,7 L7,8.5 Q3,8 1.5,3 Z" fill="#0a5a9c"/></svg>65 8100 4420</p>
    <h3 style="margin-top:9px">China Office:</h3>
    <p>上海市长乐路88弄<br>C座1203室 和园<br>邮编 200040</p>
    <p class="line"><svg class="icon" viewBox="0 0 10 10"><rect width="10" height="10" rx="2" fill="var(--yellow)"/><path d="M3,2 L4,4 L3.5,5 Q4.5,6.5 5.5,6.5 L6,6 L8,7 L7,8.5 Q3,8 1.5,3 Z" fill="#0a5a9c"/></svg>86-021-55501234</p>
    <p class="line"><svg class="icon" viewBox="0 0 10 10"><rect x="0.5" y="1.5" width="9" height="7" fill="var(--yellow)"/><path d="M0.5,1.5 L5,5.5 L9.5,1.5" stroke="#0a5a9c" fill="none"/></svg>info@kirava.org</p>
    <h3 style="margin-top:14px">Social Networks:</h3>
    <p class="line"><span class="dot"></span>social/Kirava Art<br>and Culture Exchange</p>
    <p class="line"><span class="dot"></span>@kirava_singapore</p>
    <p class="line"><span class="dot"></span>@KVmira</p>
    <p class="line"><span class="dot"></span>boards/kirava-moments</p>
  </div>

  <div class="block brand" style="left:560px;top:16px;font-size:13px"><span class="mark"></span><span>KIRAVA<br><span style="font-size:10px">Art &amp; Exchange</span></span></div>
  <div class="block headline" style="left:482px;top:86px;width:238px">
    <div class="one">OPENING MINDS</div>
    <div class="two">TOUCHING HEARTS</div>
  </div>
  <div class="web">www.kirava.org</div>
</section>

<!-- Inner spread -->
<section class="spread spread--inner">
  <svg class="art" viewBox="0 0 720 510" preserveAspectRatio="none">
    <defs>
      <linearGradient id="iGrey" x1="0" y1="0" x2="1" y2="1"><stop offset="0" stop-color="#f8f8f8"/><stop offset="1" stop-color="#d6d6d6"/></linearGradient>
      <linearGradient id="iBlue" x1="0" y1="0" x2="0" y2="1"><stop offset="0" stop-color="#1a8fd6"/><stop offset="1" stop-color="#2db0e8"/></linearGradient>
      <linearGradient id="iRed" x1="0" y1="0" x2="1" y2="0"><stop offset="0" stop-color="#c70f19"/><stop offset="1" stop-color="#ea2b30"/></linearGradient>
      <linearGradient id="iLawn" x1="0" y1="0" x2="0" y2="1"><stop offset="0" stop-color="#7d8c6e"/><stop offset=".55" stop-color="#b9ad96"/><stop offset="1" stop-color="#3f8a3c"/></linearGradient>
      <linearGradient id="iTrunk" x1="0" y1="0" x2="1" y2="1"><stop offset="0" stop-color="#6d6a63"/><stop offset="1" stop-color="#3a5f8c"/></linearGradient>
      <linearGradient id="iPlay" x1="0" y1="0" x2="1" y2="1"><stop offset="0" stop-color="#c9bcae"/><stop offset=".5" stop-color="#c23a3a"/><stop offset="1" stop-color="#3c4a5e"/></linearGradient>
    </defs>
    <rect width="720" height="510" fill="url(#iGrey)"/>
    <path role="img" aria-label="Red-toned photo: volunteers sharing a meal" d="M262,0 H500 V110 C430,120 330,105 262,90 Z" fill="#b50d16"/>
    <path d="M0,0 H262 V90 C170,70 80,80 0,110 Z" fill="url(#iRed)"/>
    <path d="M0,110 C110,70 240,70 330,100 C420,130 470,140 720,100" fill="none" stroke="var(--yellow)" stroke-width="9"/>
    <path role="img" aria-label="Photo: volunteer playing with two toddlers on a lawn" d="M22,98 H258 V290 H22 Z" fill="url(#iLawn)"/>
    <path role="img" aria-label="Photo: volunteer caring for an elephant" d="M258,112 C300,118 350,125 392,128 C385,180 378,240 382,290 H258 Z" fill="url(#iTrunk)"/>
    <path d="M392,128 C384,180 378,240 382,290 C384,360 390,440 395,510" fill="none" stroke="var(--yellow)" stroke-width="8"/>
    <path role="img" aria-label="Photo: children and volunteers waving in a classroom" d="M0,290 H382 C384,360 388,440 391,510 H0 Z" fill="url(#iPlay)"/>
    <path d="M500,175 C580,160 650,140 720,115 V510 H500 Z" fill="url(#iBlue)"/>
    <path d="M500,175 C580,160 650,140 720,115" fill="none" stroke="#ffffff" stroke-width="3"/>
    <path role="img" aria-label="Faint photo: students gathered together" d="M500,355 H720 V510 H500 Z" fill="#ffffff" opacity=".18"/>
  </svg>

  <div class="block brand" style="left:525px;top:35px;font-size:16px"><span class="mark" style="width:20px;height:20px"></span><span>KIRAVA<br><span style="font-size:12px">Art &amp; Exchange</span></span></div>

  <div class="block" style="left:500px;top:182px;width:215px">
    <span class="tab">Our Vision:</span>
    <p class="white-copy" style="margin:6px 0 0 8px">A world more at peace and in harmony through cultural appreciation, education and learning.</p>
    <span class="tab" style="margin-top:8px">What We Provide:</span>
    <p class="sub" style="margin:6px 0 2px 8px">Our Programs:</p>
    <ul class="programs" style="margin-left:8px">
      <li>International Volunteer Program</li>
      <li>International Internship Program</li>
      <li>International High School Exchange Program</li>
      <li>Group Student Program</li>
      <li>Independent Home Stays</li>
      <li>Language Courses</li>
    </ul>
  </div>

  <div class="partners-label">PARTNERS</div>
  <div class="partner" style="top:315px"><div class="badge-square"></div>Volunteers for<br>Global Fellowship</div>
  <div class="partner" style="top:395px"><div class="badge-circle"></div>Federation for Shared<br>Living Abroad</div>
</section>

</body>
</html>
```